A DL (210mm wide x 100mm deep) layered .psd prepared for print ready CMYK 300 dpi for gloss paper.

Target Market(s)

Business People & young professionals – middle – high income earners.

Requirements
Must have
• Heading:
TOP Brunch (big and bold)
Traders Owners Partners (smaller underneath)

Text:
Everything about the TOP Brunch is TOP. The TOP Brunches are aimed at Traders, Owners and Partners and are designed to be an environment for where people Thrive, Offer and Prosper, while learning Trade, Openness and Prudence.

These events will be held on Friday mornings at 7am on February 17, May 18, August 17 and November 16, 2012.

The Velvet Playhouse, 412 Marlow Lane, Newcastle.
For more information, Phone (02) 4813 5062 or email info@chapel365.example

Please include:
SFP Logo, Chapel365 Logo, & TOP Logo
Nice to have
• Open to blue colours refer to steadyfundplanning.example and Chapel365.example

- Open to graphics/illustrations/photos - Can also purchase images from PixVault.
Should not have
• Too Much Bright Red or Yellow (open to some but not like a Burgertown flyer)

```html
<!DOCTYPE html>
<html lang="en">
<head>
<meta charset="utf-8">
<title>TOP Brunch – Traders Owners Partners</title>
<link rel="stylesheet" href="https://fonts.googleapis.com/css2?family=Archivo+Black&family=Lato:wght@300;400&display=swap">
<style>
  :root {
    --frame-blue: #2a9fd8;
    --headline-blue: #16a8e8;
    --ink-navy: #1c3550;
    --band-green: #b3d236;
    --box-border: #a9cf4a;
    --contact-blue: #2aa9e0;
    --paper: #ffffff;
    --photo-deep: #1d5d95;
    --photo-mid: #6fa6d2;
    --photo-light: #e3eff8;
  }
  * { margin: 0; padding: 0; box-sizing: border-box; }
  html, body { width: 1200px; height: 588px; overflow: hidden; background: var(--paper); }
  .flyer {
    position: relative; width: 1200px; height: 588px; background: var(--paper);
    font-family: "Lato", Arial, sans-serif;
  }
  .flyer-frame {
    position: absolute; left: 21px; top: 16px; width: 1158px; height: 553px;
    border: 2px solid var(--frame-blue); overflow: hidden; background: var(--paper);
  }
  .hero-photo {
    position: absolute; left: 0; top: 0; width: 100%; height: 438px;
    background:
      linear-gradient(90deg, var(--photo-deep) 0%, var(--photo-mid) 35%, rgba(227,239,248,0.6) 55%, var(--photo-light) 100%),
      linear-gradient(180deg, var(--photo-mid), var(--photo-light));
  }
  .headline {
    position: absolute; right: 32px; top: 30px;
    font-family: "Archivo Black", "Arial Black", sans-serif;
    font-size: 86px; line-height: 1; letter-spacing: 2px;
    color: var(--headline-blue);
    -webkit-text-stroke: 2px var(--paper);
    paint-order: stroke fill;
  }
  .subheading {
    position: absolute; right: 32px; top: 104px;
    font-size: 19px; font-weight: 400; letter-spacing: 9px;
    color: var(--ink-navy);
  }
  .event-copy {
    position: absolute; right: 34px; top: 155px; width: 640px;
    text-align: right; font-weight: 300; font-size: 21px; line-height: 25px;
    color: var(--ink-navy);
  }
  .event-copy p + p { margin-top: 14px; }
  .venue-band {
    position: absolute; left: 0; top: 438px; width: 100%; height: 45px;
    background: var(--band-green);
  }
  .venue {
    position: absolute; left: 30px; top: 11px;
    font-weight: 300; font-size: 21px; color: var(--ink-navy);
  }
  .partner-logos {
    position: absolute; left: 628px; top: 359px; display: flex; gap: 5px;
  }
  .partner-box {
    width: 165px; height: 114px; background: var(--paper);
    border: 2px solid var(--box-border); border-radius: 14px;
    display: flex; align-items: center; justify-content: center;
    padding: 0 10px; overflow: hidden;
    font-family: "Archivo Black", "Arial Black", sans-serif;
    font-size: 24px; color: var(--ink-navy); white-space: nowrap;
  }
  .contact {
    position: absolute; left: 0; top: 502px; width: 100%;
    text-align: center; font-weight: 300; font-size: 21px; letter-spacing: 0.4px;
    color: var(--contact-blue); text-transform: uppercase;
  }
</style>
</head>
<body>
<main class="flyer">
  <div class="flyer-frame">
    <div class="hero-photo" role="img" aria-label="Photo of two young business professionals smiling at a laptop in front of blue glass office towers"></div>

    <h1 class="headline">TOP BRUNCH</h1>
    <p class="subheading">TRADERS OWNERS PARTNERS</p>

    <div class="event-copy">
      <p>These events will be held on Friday mornings at 7am on February 17, May 18, August 17 and November 16, 2012.</p>
      <p>Everything about the TOP Brunch is TOP. The TOP Brunches are aimed at Traders, Owners and Partners and are designed to be an environment for where people Thrive, Offer and Prosper, while learning Trade, Openness and Prudence.</p>
    </div>

    <div class="venue-band">
      <p class="venue">THE VELVET PLAYHOUSE, 412 MARLOW LANE, NEWCASTLE.</p>
    </div>

    <div class="partner-logos">
      <div class="partner-box">SFP</div>
      <div class="partner-box">TOP</div>
      <div class="partner-box">Chapel365</div>
    </div>

    <p class="contact">For more information, phone (02) 4813 5062 or email info@chapel365.example</p>
  </div>
</main>
</body>
</html>
```